Are Your Bloom Harbor? Innovative Company Needs a Web Design *Guaranteed*

We need a web design for our coaching company that helps college women overcome depression and anxiety without the stigma or hassle of traditional therapy. Ultimately, we need a website that conveys that we are the world's leading experts in this area. That is our focus. It must invite a very trusting and free spirited feminine atmoshpere that a college girl would cherish and would not hesitate to revist again and again. We need a balance of being the experts and being a laid-back party spot, a place where our college clients become absolute raving fans of our service and take action. It should be easy on the eyes, great to look at, and makes a awesome first impression. We would like to see the color scheme match our logo coloring as well.

Target Market(s)

College Women

Requirements
Must have
• Social media integration is vital. This webpage should also be mobile friendly, a good balance of flash and flow yet simplicity. It must follow the placement format we have provided. Arial, Verdana fonts preferred. Our objective is for them to "see what we are all about" in just a glimpse of the page, without scrolling down or actions, more specifically to draw ALL attention to watch our pitch video.
Nice to have
• Since our logo has a flower on it, Im curious to see what can be done with that coloring. Perhaps a tropic of Hawaiian theme? Plants are metaphoric for growth and are always a nice background. A pop-up upon entering page to capture emails for free content would be really nice to collect their name, cell, email, biggest challenge.
Should not have
• No ugly colors. Nothing that is to serious. And most importantly, we want to convey we are experts. The design cannot give the impression that we are some large, dark, ominous company with a shady agenda. College students do not trust companies like this especially since most are only out for their money. We want to separate ourselves from the pack and prove we are all about them and always on their side.

```html
<!DOCTYPE html>
<html lang="en">
<head>
<meta charset="utf-8">
<title>Bloom Harbor – Coaching for College Women</title>
<link rel="stylesheet" href="https://fonts.googleapis.com/css2?family=Arimo:wght@400;700&family=Rosarivo&display=swap">
<style>
:root{
  --page:#f7f4ea;
  --card:#ffffff;
  --blue:#0a74c4;
  --blue-dark:#0360b0;
  --blue-light:#1d8fe2;
  --video:#3fb1e3;
  --pink:#e8167d;
  --text:#333333;
  --muted:#7a7a7a;
  --rule:#e6e6e6;
  --sans:"Arimo",Arial,sans-serif;
  --serif:"Rosarivo",Georgia,serif;
}
*{box-sizing:border-box;margin:0;padding:0}
html,body{width:1062px;height:1200px;overflow:hidden}
body{position:relative;background:var(--page);font-family:var(--sans);color:var(--text)}
.abs{position:absolute}
.card{left:79px;top:18px;width:904px;height:1107px;background:var(--card);border-radius:6px}
/* header */
.brand{left:90px;top:70px;display:flex;align-items:center;gap:12px}
.brand-dot{width:38px;height:38px;border-radius:50%;background:var(--pink)}
.brand-name{font-family:var(--sans);font-weight:700;font-size:30px;color:var(--blue);letter-spacing:-.5px}
.social{top:49px;width:28px;height:28px;border-radius:50%;border:2px solid #d4d4d4;background:#9fb3c8}
.social.s2{background:#7fc7e2}.social.s3{background:#f0a06a}
.search{left:561px;top:51px;width:148px;height:24px;border:1px solid #cfcfcf;background:#fff;font-size:11px;padding:6px 12px;color:#444}
.search svg{position:absolute;right:8px;top:4px}
.nav{left:438px;top:107px;width:540px;height:34px;border-radius:17px;overflow:hidden;display:flex;background:linear-gradient(var(--blue-light),var(--blue-dark))}
.nav a{display:flex;align-items:center;justify-content:center;color:#fff;font-size:13.5px;text-decoration:none;border-right:1px solid rgba(0,0,0,.18)}
.nav a:last-child{border-right:0}
.nav a.active{background:linear-gradient(#f2479b,#d80f6d)}
.quote{left:79px;top:188px;width:904px;text-align:center;font-family:var(--serif);font-size:21px;color:#8a8a8a;letter-spacing:.3px}
/* hero */
.hero{left:83px;top:231px;width:895px;height:300px;background:linear-gradient(180deg,#4fb7ea 0%,#a9dcf3 40%,#cfe7ee 58%,#ece8df 75%,#e3ddd2 100%)}
.hero-title{left:109px;top:366px;font-family:var(--serif);font-size:21.5px;line-height:28px;color:var(--pink);text-shadow:0 0 2px #fff,0 0 2px #fff,1px 1px 1px #fff}
.hero-copy{left:109px;top:440px;width:300px;font-size:12.5px;line-height:18.5px;color:#222;text-align:justify}
.video-frame{left:443px;top:238px;width:523px;height:302px;background:#fff;box-shadow:0 6px 8px -4px rgba(0,0,0,.3)}
.video{left:450px;top:244px;width:510px;height:290px;background:var(--video)}
/* thumbnails */
.thumb{top:580px;width:204px;height:111px;border:1px solid #e2e2e2;background:#fff;padding:6px}
.thumb div{width:100%;height:100%}
.thumb-label{position:absolute;left:6px;top:6px;right:6px;bottom:6px;display:flex;align-items:center;justify-content:center;text-align:center;font-family:var(--serif);font-size:19px;line-height:24px;color:#fff;text-shadow:0 1px 2px rgba(0,0,0,.6)}
.arrow{top:624px}
.divider{left:95px;top:716px;width:865px;height:1px;background:var(--rule)}
/* content */
.section-title{font-size:19px;color:var(--blue)}
.rule{height:1px;background:var(--rule)}
.kicker{font-size:13px;color:var(--pink)}
.body-copy{font-size:11.5px;line-height:18.5px;color:var(--muted);text-align:justify}
.photo{border:1px solid #ddd;box-shadow:1px 1px 2px rgba(0,0,0,.15)}
.dot{top:757px;width:8px;height:8px;border-radius:50%;background:#a5a5a5}
.dot.on{background:var(--blue)}
.date{font-size:11.5px;color:#222}
.footer-links{left:0;top:1141px;width:1062px;text-align:center;font-size:12px;color:var(--muted);word-spacing:2px}
.footer-links span{margin:0 7px;color:#999}
.copyright{left:0;top:1169px;width:1062px;text-align:center;font-size:12px;color:var(--muted)}
</style>
</head>
<body>
<div class="abs card"></div>

<header>
  <div class="abs brand"><span class="brand-dot"></span><span class="brand-name">Bloom Harbor</span></div>
  <span class="abs social" style="left:444px" aria-label="Social link"></span>
  <span class="abs social s2" style="left:481px" aria-label="Social link"></span>
  <span class="abs social s3" style="left:518px" aria-label="Social link"></span>
  <div class="abs search">Search
    <svg width="16" height="16" viewBox="0 0 16 16"><circle cx="6" cy="6" r="4.5" fill="none" stroke="#222" stroke-width="2.2"/><line x1="9.5" y1="9.5" x2="14" y2="14" stroke="#222" stroke-width="3" stroke-linecap="round"/></svg>
  </div>
  <nav class="abs nav">
    <a class="active" style="width:79px">Home</a>
    <a style="width:86px">Product</a>
    <a style="width:84px">Parents</a>
    <a style="width:113px">How it works</a>
    <a style="width:90px">About us</a>
    <a style="width:88px">Contact</a>
  </nav>
  <p class="abs quote">“ Maecenas commodo, lectus a adipiscing sodales, tortor purus sodales ”</p>
</header>

<section>
  <div class="abs hero" role="img" aria-label="Bright tropical beach with turquoise sea and sky"></div>
  <h1 class="abs hero-title" style="font-weight:400">We helps women overcome<br>depression, stress and anxiety</h1>
  <p class="abs hero-copy">Sed accumsan, diam eget fringilla lobortis, orci quam convallis lacus, vitae aliquam dolor mi cursus turpis. Donec tellus est, ullamcorper eget aliquam in, congue ut erat. Fusce rhoncus fermentum blandit.</p>
  <div class="abs video-frame"></div>
  <div class="abs video" role="img" aria-label="Pitch video player"></div>
  <svg class="abs" style="left:671px;top:354px" width="68" height="68" viewBox="0 0 68 68">
    <defs><linearGradient id="playFill" x1="0" y1="0" x2="0" y2="1"><stop offset="0" stop-color="#ffffff"/><stop offset="1" stop-color="#b9b9b9"/></linearGradient></defs>
    <circle cx="34" cy="34" r="32" fill="url(#playFill)" stroke="#8e8e8e" stroke-width="2"/>
    <path d="M26 20 L50 34 L26 48 Z" fill="#6f6f6f"/>
  </svg>
</section>

<section>
  <svg class="abs arrow" style="left:86px" width="18" height="22" viewBox="0 0 18 22"><path d="M15 2 L5 11 L15 20" fill="none" stroke="#b5b5b5" stroke-width="4"/></svg>
  <div class="abs thumb" style="left:110px"><div role="img" aria-label="Counselor speaking with a young woman" style="background:linear-gradient(135deg,#9a9a9a,#6e6e6e)"></div><span class="thumb-label">Counseling for<br>Depression</span></div>
  <div class="abs thumb" style="left:324px"><div role="img" aria-label="Young woman looking down thoughtfully" style="background:linear-gradient(135deg,#1d3f8a,#5a3a2a 60%,#2a3a80)"></div></div>
  <div class="abs thumb" style="left:537px"><div role="img" aria-label="Woman resting her head on her hands" style="background:linear-gradient(135deg,#d9b89a,#b98466 55%,#e8d4c2)"></div></div>
  <div class="abs thumb" style="left:752px"><div role="img" aria-label="Woman behind a rainy window" style="background:linear-gradient(135deg,#1d5fa8,#0c2540 60%,#7a4a5a)"></div></div>
  <svg class="abs arrow" style="left:958px" width="18" height="22" viewBox="0 0 18 22"><path d="M3 2 L13 11 L3 20" fill="none" stroke="#b5b5b5" stroke-width="4"/></svg>
  <div class="abs divider"></div>
</section>

<section>
  <h2 class="abs section-title" style="left:96px;top:749px;font-weight:400">What we do</h2>
  <div class="abs rule" style="left:80px;top:785px;width:422px"></div>
  <p class="abs kicker" style="left:95px;top:803px">Aliquam pharetra elementum nunc.</p>
  <p class="abs body-copy" style="left:95px;top:827px;width:407px">Vestibulum tincidunt mi eget quam suscipit aliquam. Sed porttitor arcu quis massa luctus commodo. Aenean quis leo libero, ut fermentum mi. Nam eget lectus tellus. Vestibulum rutrum consequat convallis.</p>
  <p class="abs body-copy" style="left:95px;top:901px;width:202px">Cras nunc nisl, gravida a imperdiet vel, sagittis et ipsum. Curabitur sodales lacus non mi viverra tristique. Mauris nibh erat, sagittis ut tristique id, vulputate sed nulla. Morbi feugiat placerat leo, non tempor felis sodales id. Pellentesque commodo tristique metus, id tristique ipsum ornare non. Vestibulum bibendum, dolor venenatis porttitor fermentum, justo neque porttitor nibh, vel.</p>
  <div class="abs photo" role="img" aria-label="Flowers resting on a wooden casket outdoors" style="left:315px;top:909px;width:186px;height:168px;background:linear-gradient(180deg,#4a5a3a,#6a4a30 55%,#2a2a2a)"></div>

  <h2 class="abs section-title" style="left:550px;top:749px;font-weight:400">What students are saying?</h2>
  <span class="abs dot on" style="left:890px"></span>
  <span class="abs dot" style="left:909px"></span>
  <span class="abs dot" style="left:929px"></span>
  <span class="abs dot" style="left:948px"></span>
  <div class="abs rule" style="left:537px;top:785px;width:431px"></div>

  <div class="abs photo" role="img" aria-label="Portrait of a student" style="left:550px;top:805px;width:112px;height:75px;background:linear-gradient(135deg,#111,#5a3a2a 50%,#111)"></div>
  <p class="abs kicker" style="left:680px;top:803px">Aliquam pharetra elementum nunc.</p>
  <p class="abs body-copy" style="left:680px;top:828px;width:280px;line-height:16.5px;text-align:left">Vestibulum tincidunt mi eget quam suscipit aliquam. Sed porttitor arcu quis massa luctus commodo.</p>
  <p class="abs date" style="left:680px;top:870px">Apr-2-2013</p>

  <div class="abs photo" role="img" aria-label="Student in conversation with a counselor" style="left:550px;top:908px;width:112px;height:75px;background:linear-gradient(135deg,#cfe0ec,#8fb0cc 50%,#e8d8c8)"></div>
  <p class="abs kicker" style="left:680px;top:906px">Aliquam pharetra elementum nunc.</p>
  <p class="abs body-copy" style="left:680px;top:931px;width:280px;line-height:16.5px;text-align:left">Vestibulum tincidunt mi eget quam suscipit aliquam. Sed porttitor arcu quis massa luctus commodo.</p>
  <p class="abs date" style="left:680px;top:973px">Apr-2-2013</p>

  <div class="abs photo" role="img" aria-label="Students in a relaxation class" style="left:550px;top:1019px;width:112px;height:75px;background:linear-gradient(135deg,#eef2f4,#c9d6dd 50%,#e4cfbf)"></div>
  <p class="abs kicker" style="left:680px;top:1017px">Aliquam pharetra elementum nunc.</p>
  <p class="abs body-copy" style="left:680px;top:1042px;width:280px;line-height:16.5px;text-align:left">Vestibulum tincidunt mi eget quam suscipit aliquam. Sed porttitor arcu quis massa luctus commodo.</p>
  <p class="abs date" style="left:680px;top:1084px">Apr-2-2013</p>
</section>

<footer>
  <p class="abs footer-links">Home<span>|</span>Product<span>|</span>Parents<span>|</span>How it works<span>|</span>About us<span>|</span>Contact</p>
  <p class="abs copyright">Copyright &copy; 2013 &nbsp; www.bloomharbor.com &nbsp; All rights reserved.</p>
</footer>
</body>
</html>
```